" Quintela advogados é um escritório de advocacia de grande porte atuando em 6 Estados, sendo em 3 deles temos filial em funcionamento, além da matriz (Curitiba). "

```html
<!DOCTYPE html>
<html lang="pt-BR">
<head>
<meta charset="utf-8">
<title>Quintela Advogados — Papel timbrado</title>
<link href="https://fonts.googleapis.com/css2?family=Cinzel:wght@500&family=Montserrat:wght@500;600&display=swap" rel="stylesheet">
<style>
  :root {
    --backdrop: #e9e9e7;
    --paper: #ffffff;
    --ink: #1b1b1b;
    --navy: #1c2442;
    --watermark: #ececec;
    --shadow: rgba(0,0,0,0.28);
  }
  * { margin: 0; padding: 0; box-sizing: border-box; }
  html, body {
    width: 1200px; height: 1200px; overflow: hidden;
    background: var(--backdrop);
  }
  .letterhead {
    position: absolute;
    left: 195px; top: 50px;
    width: 810px; height: 1100px;
    background: var(--paper);
    box-shadow: 0 8px 24px var(--shadow);
  }
  .brand {
    position: absolute;
    top: 40px; left: 0; right: 0;
    text-align: center;
    color: var(--ink);
  }
  .brand-mark {
    display: block;
    width: 46px; height: 46px;
    margin: 0 auto 44px;
    background: var(--ink);
  }
  .brand-name {
    font-family: "Cinzel", serif;
    font-weight: 500;
    font-size: 30px;
    letter-spacing: 3px;
    line-height: 1;
  }
  .brand-tag {
    margin-top: 8px;
    font-family: "Montserrat", sans-serif;
    font-weight: 600;
    font-size: 9px;
    letter-spacing: 4px;
    text-transform: uppercase;
  }
  .watermark {
    position: absolute;
    top: 500px; left: 0; right: 0;
    text-align: center;
    font-family: "Cinzel", serif;
    font-weight: 500;
    font-size: 104px;
    letter-spacing: 6px;
    line-height: 1;
    color: var(--watermark);
    user-select: none;
  }
  .contact {
    position: absolute;
    right: 40px; top: 951px;
    height: 86px;
    padding-right: 12px;
    border-right: 4px solid var(--navy);
    display: flex; flex-direction: column; justify-content: flex-end;
    text-align: right;
    font-family: "Montserrat", sans-serif;
    font-weight: 600;
    font-size: 13px;
    line-height: 20px;
    color: var(--navy);
    list-style: none;
  }
</style>
</head>
<body>
  <main class="letterhead">
    <header class="brand">
      <span class="brand-mark" aria-hidden="true"></span>
      <div class="brand-name">Quintela</div>
      <div class="brand-tag">Advogados</div>
    </header>

    <div class="watermark" aria-hidden="true">QUINTELA</div>

    <ul class="contact">
      <li>+55 41 3021-5840</li>
      <li>+55 41 3355-1902</li>
      <li>contato@quintela.adv.br</li>
      <li>www.quintela.adv.br</li>
    </ul>
  </main>
</body>
</html>
```